Job Coaching - Vanta; engaging people to improve their work experience

I need a flyer for Job Coaching. It serves to engage customers (not businesses) with problems in their daily job, typical questions that are handled are:
Do I fit for the job?
Am I using my talents at best in this job?
I have a conflict with my manager/colleagues, what should I do?
My work-life balance is a mess, how can I improve this?
What job fits best with my talents?
I'm getting stressed out from my job, what can I do?
....
This Flyer will be available at GP's, therpeutic practices, pharamcists,...
this flyer should put people in action to contact me
Flyer can be created in English, in the final one the text should be in Dutch; I will make the translation of the selected flyer and provide it at the end

Target Market(s)

consumers / customers / people having a job, but somewhat stuck in it

Industry/Entity Type

Professional Coaching

Requirements
Must have
• the questions mentioned in the project description; mobile number: 0471/389145; email: tom.vermeer@vantacoaching.example; website: www.vantacoaching.example ; it should make also reference to 'Career guidance cheques of the KWOL'

```html
<!DOCTYPE html>
<html lang="en">
<head>
<meta charset="utf-8">
<title>Vanta – Career Guidance Flyer</title>
<link href="https://fonts.googleapis.com/css2?family=League+Spartan:wght@600;700;800&family=Poppins:wght@400;500;600;700&family=Bebas+Neue&display=swap" rel="stylesheet">
<style>
  :root{
    --teal:#36a99e;
    --teal-deep:#26877e;
    --ink:#2b3438;
    --slate:#575d60;
    --sky:#c3f2f5;
    --paper:#ffffff;
    --backdrop:#eceeee;
  }
  *{margin:0;padding:0;box-sizing:border-box}
  html,body{width:1200px;height:2400px;overflow:hidden;background:var(--backdrop)}
  body{font-family:"Poppins",sans-serif;color:var(--ink);position:relative}

  .flyer{position:absolute;left:50px;top:421px;width:1100px;height:1558px;background:var(--paper);overflow:hidden;box-shadow:0 6px 24px rgba(0,0,0,.12)}
  .flyer > *{position:absolute}
  .shapes{left:0;top:0;width:1100px;height:1558px}

  .brand{left:56px;top:62px;display:flex;align-items:center;gap:22px}
  .brand-dot{width:96px;height:96px;border-radius:50%;background:var(--slate)}
  .brand-name{font-family:"League Spartan",sans-serif;font-weight:600;font-size:98px;line-height:1;color:var(--teal);letter-spacing:2px;padding-top:12px}

  .headline{left:58px;top:248px;font-family:"League Spartan",sans-serif;font-weight:800;line-height:.9}
  .headline .line-accent{display:block;font-size:98px;color:var(--teal)}
  .headline .line-main{display:block;font-size:98px;color:var(--ink);margin-top:6px}
  .headline .line-sub{display:block;font-size:44px;color:var(--slate);margin-top:12px;letter-spacing:.5px}

  .intro{top:570px;font-size:20.5px;line-height:24.5px;color:#fff}
  .intro strong{font-weight:700}
  .intro-left{left:56px;width:450px}
  .intro-right{left:584px;width:475px}

  .ribbon-text{left:150px;width:789px;top:764px;height:48px;display:flex;align-items:center;justify-content:center;font-weight:700;font-size:27px;color:#fff;white-space:nowrap}

  .questions{left:478px;top:836px;width:600px}
  .questions-title{font-family:"League Spartan",sans-serif;font-weight:800;font-size:43px;line-height:39px}
  .questions-title .title-accent{color:var(--teal);display:block}
  .questions-title .title-main{color:var(--ink)}
  .question-list{list-style:none;margin-top:24px;display:flex;flex-direction:column;gap:8px}
  .question-list li{position:relative;padding-left:24px;font-size:20.5px;line-height:24.5px;font-weight:500;max-width:580px}
  .question-list li::before{content:"?";position:absolute;left:0;top:-1px;color:var(--teal);font-weight:700;font-size:23px}

  .cheques{left:386px;top:1214px;display:flex;align-items:center;gap:12px;white-space:nowrap}
  .cheques-label{font-family:"League Spartan",sans-serif;font-weight:700;font-size:29px;line-height:27px;color:var(--ink);text-align:center;padding-top:4px}
  .cheques-name{font-family:"Bebas Neue",sans-serif;font-weight:400;font-size:72px;line-height:1;color:var(--teal);letter-spacing:.5px}

  .contact-call{left:317px;top:1328px;font-family:"League Spartan",sans-serif;font-weight:700;font-size:23px;line-height:22px;color:#fff;white-space:nowrap}
  .contact-call .call-accent{color:var(--teal)}
  .coach{left:317px;top:1400px;white-space:nowrap}
  .coach-name{font-family:"League Spartan",sans-serif;font-weight:700;font-size:30px;line-height:1;color:var(--teal)}
  .coach-role{font-family:"League Spartan",sans-serif;font-weight:700;font-size:13px;color:#fff;margin-top:3px}
  .contact-lines{left:545px;top:1392px;color:#fff;white-space:nowrap}
  .contact-line{display:flex;align-items:center;gap:10px;font-weight:500;line-height:34px}
  .contact-line svg{flex:none}
  .contact-phone{font-size:24px}
  .contact-mail{font-size:19px}
  .website{left:240px;width:761px;top:1467px;height:43px;display:flex;align-items:center;justify-content:center;font-weight:700;font-size:22px;letter-spacing:8px;color:#fff;white-space:nowrap}
</style>
</head>
<body>
<main class="flyer">
  <svg class="shapes" viewBox="0 0 1100 1558">
    <circle cx="210" cy="1052" r="242" fill="var(--slate)"/>
    <g role="img" aria-label="Illustration of a confused businessman surrounded by question marks">
      <circle cx="203" cy="1043" r="242" fill="var(--sky)"/>
    </g>
    <rect x="0" y="503" width="1100" height="309" fill="var(--ink)"/>
    <line x1="544" y1="503" x2="544" y2="770" stroke="#3d474b" stroke-width="2"/>
    <polygon points="142,812 164,760 925,760 947,812" fill="var(--teal-deep)"/>
    <polygon points="160,812 178,764 911,764 929,812" fill="var(--teal)"/>
    <circle cx="815" cy="260" r="281" fill="var(--slate)"/>
    <g role="img" aria-label="Illustration of a smiling businessman with a glowing light bulb idea">
      <circle cx="827" cy="250" r="281" fill="var(--teal)"/>
    </g>
    <line x1="870" y1="913" x2="1050" y2="913" stroke="var(--ink)" stroke-width="2.5"/>
    <circle cx="1052" cy="913" r="4.5" fill="var(--ink)"/>
    <rect x="84" y="1315" width="917" height="195" rx="32" fill="var(--ink)"/>
    <path d="M240 1467 H1001 V1478 A32 32 0 0 1 969 1510 H240 Z" fill="var(--teal)"/>
    <circle cx="180" cy="1414" r="100" fill="#fff" stroke="var(--teal)" stroke-width="2.5" stroke-dasharray="6 5"/>
    <g role="img" aria-label="Portrait photo of coach Tom Vermeer">
      <circle cx="180" cy="1414" r="88" fill="#b98a74"/>
    </g>
  </svg>

  <div class="brand">
    <span class="brand-dot"></span>
    <span class="brand-name">VANTA</span>
  </div>

  <h1 class="headline">
    <span class="line-accent">CAREER</span>
    <span class="line-main">GUIDANCE</span>
    <span class="line-sub">WITH CAREER VOUCHERS</span>
  </h1>

  <p class="intro intro-left">We easily spend 8 hours a day on our professional pursuits, our job. If we assume that we sleep about <strong>8 hours a day, that's 50% of our active time.</strong> We actually spend more time with our colleagues than with our partner and/or children.</p>
  <p class="intro intro-right">Unfortunately, not every career goes smoothly, and it is even very normal that there are ups and downs this, nowadays more than 40-year career. But <strong>we can strive to keep these downs as short as possible and the ups as long as possible.</strong></p>

  <p class="ribbon-text">And that's where Career Counseling comes into play.</p>

  <section class="questions">
    <h2 class="questions-title"><span class="title-accent">TYPICAL QUESTIONS THAT</span><span class="title-main">ARE HANDLED ARE</span></h2>
    <ul class="question-list">
      <li>Do I fit for the job?</li>
      <li>Am I using my talents at best in this job?</li>
      <li>I have a conflict with my manager/colleagues, what<br>should I do?</li>
      <li>My work-life balance is a mess, how can I<br>improve this?</li>
      <li>What job fits best with my talents?</li>
      <li>I'm getting stressed out from my job, what can I do?</li>
    </ul>
  </section>

  <div class="cheques">
    <span class="cheques-label">CAREER<br>GUIDANCE</span>
    <span class="cheques-name">CHEQUES OF THE KWOL</span>
  </div>

  <p class="contact-call"><span class="call-accent">DO YOU KNOW WHAT YOU WANT,</span> BUT DO NOT DARE<br>TO TAKE THE STEP?</p>

  <div class="coach">
    <p class="coach-name">TOM VERMEER</p>
    <p class="coach-role">PROFESSIONAL COACH</p>
  </div>

  <div class="contact-lines">
    <p class="contact-line contact-phone">
      <svg width="20" height="20" viewBox="0 0 24 24"><path d="M6.6 10.8a15.1 15.1 0 0 0 6.6 6.6l2.2-2.2a1 1 0 0 1 1-.25 11.4 11.4 0 0 0 3.6.57 1 1 0 0 1 1 1V20a1 1 0 0 1-1 1A17 17 0 0 1 3 4a1 1 0 0 1 1-1h3.5a1 1 0 0 1 1 1c0 1.25.2 2.45.57 3.57a1 1 0 0 1-.25 1z" fill="none" stroke="var(--teal)" stroke-width="2"/></svg>
      0471/389145
    </p>
    <p class="contact-line contact-mail">
      <svg width="20" height="16" viewBox="0 0 24 18"><rect x="1" y="1" width="22" height="16" rx="2" fill="var(--teal)"/><path d="M2 2l10 8 10-8" fill="none" stroke="var(--ink)" stroke-width="2"/></svg>
      tom.vermeer@vantacoaching.example
    </p>
  </div>

  <p class="website">WWW.VANTACOACHING.EXAMPLE</p>
</main>
</body>
</html>
```